International emerging specialist Research and Development Company focused on plant-based medicine

We need a powerpoint design for a new company based in British Columbia, Canada called Valtio Pharmex. We are focused on developing plant-based medicines. The company is driven by its experience in research and development work in plant genetics, cultivation techniques, natural medicines, biochemistry, agriculture and technologies. Valtio will research, develop and produce very unique and specific cultivars from the plant kingdom needed for specific ailments in medical patients. We would like to see designs that use our current logo and its colour scheme. The final design should communicate financial safety, growth, and research and development.

```html
<!DOCTYPE html>
<html lang="en">
<head>
<meta charset="utf-8">
<title>Valtio Pharmex – Project Slide</title>
<link rel="stylesheet" href="https://fonts.googleapis.com/css2?family=Roboto+Condensed:wght@300;400&family=Roboto:wght@400;700&display=swap">
<style>
  :root {
    --brand-red: #d6161e;
    --brand-red-dark: #b01c24;
    --brand-red-mid: #d9333a;
    --brand-red-soft: #de545a;
    --brand-red-bright: #cc0e14;
    --bar-grey: #8f8f8f;
    --bar-grey-dark: #808080;
    --canvas-bg: #f3f3f3;
    --footer-band: #d4d4d4;
    --text-body: #333333;
    --axis: #555555;
    --white: #ffffff;
  }
  * { margin: 0; padding: 0; box-sizing: border-box; }
  html, body { width: 1200px; height: 900px; overflow: hidden; }
  body { background: var(--canvas-bg); font-family: "Roboto", Arial, sans-serif; position: relative; }

  .slide-header {
    position: absolute; left: 0; top: 0; width: 1200px; height: 93px;
    background: var(--brand-red);
    display: flex; align-items: center; justify-content: space-between;
    padding: 0 22px 0 30px;
  }
  .slide-title {
    font-family: "Roboto Condensed", Arial, sans-serif; font-weight: 400;
    font-size: 52px; color: var(--white); letter-spacing: -0.5px;
  }
  .brand-name {
    font-family: "Roboto Condensed", Arial, sans-serif; font-weight: 300;
    font-size: 36px; color: var(--white);
    display: flex; align-items: center; gap: 10px;
  }
  .brand-dot { width: 14px; height: 14px; border-radius: 50%; background: var(--white); }

  .section-heading {
    position: absolute; left: 64px; top: 154px;
    display: flex; align-items: center; gap: 14px;
    font-weight: 700; font-size: 24px; color: var(--brand-red);
  }
  .bullet-mark { width: 14px; height: 14px; border-radius: 50%; border: 2px solid var(--brand-red); }
  .section-body {
    position: absolute; left: 100px; top: 196px; width: 1060px;
    font-size: 18.5px; line-height: 30px; color: var(--text-body);
  }

  .bar-chart { position: absolute; left: 0; top: 0; }
  .axis-label { font-family: "Roboto", Arial, sans-serif; font-size: 18px; fill: var(--text-body); }
  .chart-note { font-family: "Roboto", Arial, sans-serif; font-size: 18px; fill: var(--white); }

  .slide-footer {
    position: absolute; left: 0; bottom: 0; width: 1200px; height: 42px;
    background: var(--footer-band);
  }
</style>
</head>
<body>
  <header class="slide-header">
    <h1 class="slide-title">Project Title Here</h1>
    <div class="brand-name"><span class="brand-dot"></span>Valtio Pharmex</div>
  </header>

  <h2 class="section-heading"><span class="bullet-mark"></span>Bullet Title Heading Here Bullet Title Heading Here</h2>
  <p class="section-body">Lorem ipsum dolor sit Lorem ipsum dolor sit&nbsp; Lorem ipsum dolor sit Lorem ipsum dolor sit&nbsp; Lorem ipsum dolor sit Lorem ipsum dolor sit&nbsp; Lorem ipsum dolor sit Lorem ipsum dolor sit&nbsp; Lorem ipsum dolor sit Lorem ipsum dolor sit&nbsp; Lorem ipsum dolor sit Lorem ipsum dolor sit&nbsp; Lorem ipsum dolor sit Lorem ipsum dolor sit&nbsp; Lorem ipsum dolor sit Lorem ipsum dolor sit</p>

  <svg class="bar-chart" width="1200" height="900" viewBox="0 0 1200 900" aria-label="Bar chart">
    <g class="y-labels" text-anchor="end">
      <text class="axis-label" x="278" y="349">Lorem ipsum dolor sit</text>
      <text class="axis-label" x="278" y="398">Lorem ipsum dolor sit</text>
      <text class="axis-label" x="278" y="455">Lorem ipsum dolor sit</text>
      <text class="axis-label" x="278" y="510">Lorem ipsum dolor sit</text>
      <text class="axis-label" x="278" y="563">Lorem ipsum dolor sit</text>
      <text class="axis-label" x="278" y="623">Lorem ipsum dolor sit</text>
      <text class="axis-label" x="278" y="758">Lorem ipsum dolor sit</text>
    </g>
    <g class="bars">
      <rect x="296" y="618" width="48" height="140" fill="var(--brand-red-soft)"/>
      <rect x="354" y="507" width="60" height="251" fill="var(--brand-red-mid)"/>
      <rect x="429" y="552" width="60" height="206" fill="var(--brand-red-dark)"/>
      <rect x="501" y="633" width="59" height="125" fill="var(--bar-grey)"/>
      <rect x="576" y="720" width="64" height="38" fill="var(--brand-red-mid)"/>
      <rect x="652" y="744" width="72" height="14" fill="var(--bar-grey-dark)"/>
      <rect x="733" y="366" width="60" height="392" fill="var(--brand-red-dark)"/>
      <rect x="807" y="717" width="63" height="41" fill="var(--brand-red-bright)"/>
      <rect x="882" y="738" width="63" height="20" fill="var(--bar-grey)"/>
      <rect x="958" y="744" width="72" height="14" fill="var(--bar-grey)"/>
    </g>
    <line x1="296" y1="330" x2="296" y2="758" stroke="var(--axis)" stroke-width="1.5"/>
    <line x1="296" y1="758.5" x2="1035" y2="758.5" stroke="#cfcfcf" stroke-width="2"/>
    <text class="chart-note" x="844" y="456">Subhead here Subhead here Subhead here</text>
    <text class="chart-note" x="844" y="486">Subhead here Subhead here Subhead here</text>
  </svg>

  <footer class="slide-footer"></footer>
</body>
</html>
```